5x5 Pop Up Display, Company Logo With Text and Graphics for Tradeshow Display

Design for a 5ft x 5ft pop up trade show display that will sit on top of a table. I usually prefer clean, somewhat minimalist designs. We are a food service company but it's not a requirement to have photos of food. Design elements should compliment the table cloth that we have for the booth. The below may be included depending on the design aesthetic.
Service Provided: Daily Meal Service, Kitchen Management
"Nationwide Footprint"
"Grassroots Service"
"Fresh Scratch Cooking"
"Custom Menus"
"Made To Order Meals"

```html
<!DOCTYPE html>
<html lang="en">
<head>
<meta charset="utf-8">
<title>Hale Hearth – Tradeshow Display</title>
<link rel="stylesheet" href="https://fonts.googleapis.com/css2?family=Montserrat:wght@600;700;800&display=swap">
<style>
  :root {
    --stage: #f6e3b6;
    --paper: #f1f1f0;
    --paper-shade: #d9d9d8;
    --ink: #1c1c1c;
    --green: #86bc56;
    --green-deep: #6fa545;
    --olive: #9cb94a;
    --tan: #e7c989;
    --clay: #c98e5c;
    --mustard: #e0c24a;
    --orange: #ea5a2a;
    --amber: #f08c1c;
    --red: #e2472b;
  }
  * { box-sizing: border-box; margin: 0; padding: 0; }
  html, body { width: 1200px; height: 543px; overflow: hidden; }
  body {
    background: var(--stage);
    font-family: "Montserrat", Arial, sans-serif;
    display: flex; align-items: center; justify-content: center;
  }
  .display {
    position: relative; width: 503px; height: 503px; overflow: hidden;
    background:
      radial-gradient(ellipse at 75% 30%, var(--paper-shade) 0%, transparent 45%),
      radial-gradient(ellipse at 20% 70%, #e4e4e3 0%, transparent 50%),
      var(--paper);
    box-shadow: 0 6px 18px rgba(0,0,0,.18);
    color: var(--ink);
  }
  .brand {
    position: absolute; top: 28px; left: 0; right: 0;
    text-align: center; font-weight: 800; font-size: 40px; line-height: 40px;
    letter-spacing: 1px;
  }
  .brand-mark {
    position: absolute; top: 40px; left: 318px; width: 22px; height: 22px;
    border-radius: 50%; background: var(--green);
  }
  .headline {
    position: absolute; top: 145px; left: 0; right: 0; text-align: center;
    font-weight: 700; font-size: 26px; color: var(--green);
    letter-spacing: .3px;
  }
  .rule {
    position: absolute; top: 187px; left: 136px; width: 231px; height: 4px;
    background: linear-gradient(90deg, var(--olive) 0 25%, var(--green) 25% 50%, var(--clay) 50% 75%, var(--mustard) 75% 100%);
  }
  .services {
    position: absolute; top: 224px; left: 80px; width: 380px;
    display: grid; grid-template-columns: 206px 1fr; row-gap: 13px;
    list-style: none;
  }
  .service {
    position: relative; padding-left: 9px;
    font-weight: 700; font-size: 14.5px; line-height: 16.5px; text-transform: uppercase;
  }
  .service::before {
    content: ""; position: absolute; left: 0; top: 2px; bottom: 2px; width: 4px;
    background: var(--bar);
  }
  .service.green { --bar: var(--olive); }
  .service.red { --bar: var(--red); }
  .service.amber { --bar: var(--amber); }
  .tagline {
    position: absolute; top: 380px; left: 0; right: 0; text-align: center;
    font-weight: 600; font-size: 20px; line-height: 21px; color: #333;
  }
  .tagline strong { display: block; font-weight: 700; color: var(--orange); }
  .tagline-rule {
    position: absolute; top: 427px; left: 206px; width: 92px; height: 4px;
    background: var(--orange);
  }
  .wave { position: absolute; left: 0; bottom: 0; width: 503px; height: 503px; }
</style>
</head>
<body>
  <main class="display">
    <div class="brand">HALE<br>HEARTH</div>
    <span class="brand-mark"></span>

    <h1 class="headline">SERVICE ARE PROVIDED</h1>
    <div class="rule"></div>

    <ul class="services">
      <li class="service green">Daily<br>Meal Service</li>
      <li class="service green">Grassroots<br>Service</li>
      <li class="service green">Kitchen<br>Management</li>
      <li class="service green">Fresh Scratch<br>Cooking</li>
      <li class="service red">Nationwide<br>Footprint</li>
      <li class="service amber">Custom<br>Menus</li>
    </ul>

    <p class="tagline">MADE TO<strong>ORDER MEALS</strong></p>
    <div class="tagline-rule"></div>

    <svg class="wave" viewBox="0 0 957 957" preserveAspectRatio="none" aria-hidden="true">
      <path fill="var(--tan)" d="M600,905 C790,905 890,850 957,785 L957,957 L600,957 Z"/>
      <path fill="var(--green)" d="M0,860 C150,812 300,830 450,872 C620,918 820,920 957,832 L957,957 L0,957 Z"/>
    </svg>
  </main>
</body>
</html>
```